April 11th Event- Islamorada- Coaching/Tarot/Hypnotherapy

Hi! Need a flyer that can also be posted on social media. Directions attached. Also will need a version that 2 can fit on 1 piece of paper so I can cut in half for hand outs. PDF example attached as well so you can understand. Thank you!

AAAAAAAAAAAAAAAAAAAAAAAAAAAAAAAAAAAAAAAAAAAAAAAAAAAAAAAAAAAAAAAAAAAAAAAAAAAAAAAAAAAAAAAAAAAAAAAAAAAAAAAAAAAAAAAAAAAAAAAAAAAAAAAAAAAAAAAAAAAAAAAAAAAAAAAAAAAAAAAAAAAAAAAAAAAAAAAAAAAAAAAAAAAAAAAAAAAAAAAAAAAAAAAAAAAAAAAAAAAAAAAAAA

Target Market(s)

Female audience age 35-70.
Spiritual, sophisticated

Industry/Entity Type

Event Planning

Font styles to use
Serif

Colors
d2a4cc
3176b5
85acd3
b868aa
e667a6
eea4c8
f59296
fbf289
add136

Requirements
Must have
• See attachments
Nice to have
• See attachments

```html
<!DOCTYPE html>
<html lang="en">
<head>
<meta charset="utf-8">
<title>Get the 411 – An Evening of Self Discovery</title>
<link href="https://fonts.googleapis.com/css2?family=Uncial+Antiqua&family=Lora:wght@600;700&family=Lato:ital,wght@0,300;0,400;1,300&display=swap" rel="stylesheet">
<style>
  :root {
    --purple: #6b2f73;
    --ink: #111111;
    --teal: #35b3c6;
    --rule: #7a3f82;
  }
  * { margin: 0; padding: 0; box-sizing: border-box; }
  html, body { width: 1200px; height: 1200px; overflow: hidden; background: #fff; }
  .canvas { position: relative; width: 1200px; height: 1200px; background: #fff; }

  .flyer {
    position: absolute; left: 74px; top: 232px; width: 1052px; height: 734px; overflow: hidden;
    background:
      radial-gradient(ellipse 300px 200px at 380px 80px, rgba(245,146,150,.55), transparent 70%),
      radial-gradient(ellipse 320px 240px at 330px 330px, rgba(251,242,137,.7), transparent 70%),
      radial-gradient(ellipse 260px 200px at 600px 260px, rgba(173,209,54,.22), transparent 70%),
      radial-gradient(ellipse 300px 220px at 880px 520px, rgba(133,214,235,.6), transparent 70%),
      radial-gradient(ellipse 260px 240px at 960px 140px, rgba(210,164,204,.55), transparent 70%),
      radial-gradient(ellipse 260px 220px at 180px 520px, rgba(238,164,200,.5), transparent 70%),
      radial-gradient(ellipse 300px 200px at 620px 90px, rgba(238,164,200,.35), transparent 70%),
      #fdf7f4;
  }

  .floral { position: absolute; top: 0; height: 734px; width: 146px; }
  .floral--left { left: 0; background: linear-gradient(180deg, rgba(184,104,170,.28), rgba(210,164,204,.22) 50%, rgba(184,104,170,.3)); }
  .floral--right { right: 0; background: linear-gradient(180deg, rgba(184,104,170,.28), rgba(133,172,211,.3) 50%, rgba(184,104,170,.3)); }

  .headline {
    position: absolute; left: 0; width: 100%; top: 36px; text-align: center;
    font-family: "Uncial Antiqua", serif; color: var(--purple);
    font-size: 70px; line-height: 80px; text-transform: uppercase; letter-spacing: -1px;
    white-space: nowrap;
  }
  .tagline {
    position: absolute; left: 0; width: 100%; top: 128px; text-align: center;
    font-family: "Uncial Antiqua", serif; color: var(--ink);
    font-size: 30px; line-height: 40px; text-transform: uppercase; white-space: nowrap;
  }
  .invite {
    position: absolute; left: 0; width: 100%; top: 226px; text-align: center;
    font-family: "Lora", serif; font-weight: 700; font-size: 21px; line-height: 29px; color: var(--ink);
  }
  .rule { position: absolute; left: 230px; width: 610px; height: 1px; background: var(--rule); }
  .rule--top { top: 304px; }
  .rule--bottom { top: 448px; }

  .details { position: absolute; left: 234px; top: 316px; font-family: "Lato", sans-serif; font-size: 19px; line-height: 30px; color: var(--ink); }
  .details__row { display: flex; white-space: nowrap; }
  .details__label { width: 74px; font-weight: 400; }
  .details__value { font-weight: 300; }

  .speakers { position: absolute; left: 234px; top: 460px; font-family: "Lato", sans-serif; color: var(--ink); }
  .speakers__title { font-family: "Lora", serif; font-weight: 600; color: var(--purple); font-size: 22px; line-height: 30px; }
  .speaker { font-size: 18px; line-height: 25.5px; white-space: nowrap; }
  .speaker__name { font-weight: 400; }
  .speaker__role { font-weight: 300; font-style: italic; font-size: 16px; }

  .tickets {
    position: absolute; left: 230px; top: 582px; width: 116px; height: 116px; border-radius: 50%;
    background: var(--teal); color: #fff; text-align: center; font-family: "Lato", sans-serif;
  }
  .tickets__label { display: block; margin-top: 24px; font-size: 17px; font-weight: 400; line-height: 22px; letter-spacing: .3px; }
  .tickets__price { display: block; font-family: "Lora", serif; font-size: 46px; line-height: 48px; font-weight: 600; }
  .tickets__price sup { font-size: 22px; vertical-align: 16px; }

  .info { position: absolute; left: 380px; top: 590px; font-family: "Lato", sans-serif; color: var(--ink); }
  .info__note { font-size: 19px; font-weight: 300; line-height: 28px; }
  .info__heading { font-size: 18px; font-weight: 400; line-height: 24px; margin-top: 6px; }
  .info__line { font-size: 17px; font-weight: 300; line-height: 22px; }

  .signoff {
    position: absolute; left: 714px; top: 628px; font-family: "Lora", serif; font-weight: 700;
    color: var(--purple); font-size: 24px; line-height: 25px; transform: rotate(-8deg); text-align: center;
    white-space: nowrap;
  }
</style>
</head>
<body>
<div class="canvas">
  <section class="flyer">
    <div class="floral floral--left" role="img" aria-label="Hand-drawn purple floral border of leaves and blossoms"></div>
    <div class="floral floral--right" role="img" aria-label="Hand-drawn purple floral border of leaves and blossoms"></div>

    <h1 class="headline">Get the 411</h1>
    <p class="tagline">Open Yourself Up to<br>the Info You Have Inside</p>
    <p class="invite">Please Join Us For An Evening of<br>Self Discovery, and Enlightment and Fun!</p>

    <div class="rule rule--top"></div>
    <div class="details">
      <div class="details__row"><span class="details__label">When:</span><span class="details__value">Thursday April 11th</span></div>
      <div class="details__row"><span class="details__label">Time:</span><span class="details__value">Doors Open at 5:30.&nbsp; Event from 6pm-8pm.</span></div>
      <div class="details__row"><span class="details__label">Where:</span><span class="details__value">The Gardens at Coral Lane- 81400 Seaside Highway Palm Key</span></div>
      <div class="details__row"><span class="details__label"></span><span class="details__value">(MM81 Bayside behind Market Hall)</span></div>
    </div>
    <div class="rule rule--bottom"></div>

    <div class="speakers">
      <h2 class="speakers__title">Speakers</h2>
      <p class="speaker"><span class="speaker__name">Marisol Vane</span> - <span class="speaker__role">The Kind Path Life Coach- Certified Professional Life Coach</span></p>
      <p class="speaker"><span class="speaker__name">Celeste Bramley</span> - <span class="speaker__role">Licensed Hypnotherapist- Moonrise Holistic Gifts and Care</span></p>
      <p class="speaker"><span class="speaker__name">June Sorrell</span> - <span class="speaker__role">Tarot Readings/ Open Way Spiritual Counselor</span></p>
    </div>

    <div class="tickets">
      <span class="tickets__label">TICKETS</span>
      <span class="tickets__price"><sup>$</sup>15</span>
    </div>

    <div class="info">
      <p class="info__note">Drinks included. Names must be on the guest list.</p>
      <p class="info__heading">Contact Marisol Vane for tickets:</p>
      <p class="info__line">marisol@kindpathcoach.example</p>
      <p class="info__line">305-555-0142</p>
    </div>

    <p class="signoff">Hope to<br>see you there!</p>
  </section>
</div>
</body>
</html>
```